Flyer Design Project for Harbor Tidy Works Inc.

We require a double sided marketing flyer 8 1/2 x 11. The flyer will also be marketed via e-mail using one or both sides. "Outside of the box" but yet "professional" marketing is what we'd like to achieve.

Harbor Tidy Works Inc., is a building service company providing cleaning, caretaking and concierge service to residential/stratas (condominiums/apartments)...(These services are usually provided during daytime hours). and janitorial service to commercial buildings ( service provided at night time).

- 100% green cleaning chemicals and systems
- Professionally trained staff
- Customer service is #1 priority
- Excellent Communication systems

Brochure to be 2 pages.:

Side 1: marketing residential/strata building services with a focus on providing cleaning services with a sub-focus on caretaking and concierge. We also provide move-in/out service where we coordinate with tenants to arrange access to the building, elevators and provide security (no moving involved)

Side 2: marketing night time janitorial service to property managers, corporate head offices, small offices, industrial facilities

http://www.gleamnest-home.com/index.php

http://www.brightholdpc.ca/services

These websites are from the best maid cleaning business and best strata//residential cleaning business in the city. The maid website is "you" focused, that works! The other is very straight forward and to the point, which also works.

At the end of the day our target audience ( property managers and building owners ) want us to take away one of their biggest headaches - "CLEANING". They have better things to be doing than dealing with whether or not the elevator is clean! That's our job! We're in the CLEANING business and when they don't hear a word from any of their tenants, we're doing our job and they're HAPPY :) WE TAKE AWAY HEADACHES AND MAKE PEOPLE HAPPY!

very multi-cultural target audience!

HOW CAN WE SHOW THEM IN A FLYER? THAT'S THE CHALLENGE! AND THE WINNING DESIGNER WILL BE THE ONE WHO CAN EFFECTIVELY COMMUNICATE THIS IN 1-2 PAGES.
Updates

Thank you all very much. Varolinda and Tulip, your designs are very encouraging.

Design 1223617: The layout is close to what we are hoping to achieve as it may also be incorporated into a web site homepage with each block used as a link to more info. The pictures however, make it look like any other company flyer.

Design 1224020: Also a very good layout but again not liking the pictures.

Overall, some of the designs are a little to busy with information. I would like to see something just a little more simple and yet unique that stands out against other companies.

Look forward to the second round. Thank you all very much!

Please see the new files called commercial building pics, residential strata pics and misc pics that you can use in the brochure. These are the types of pictures I would like included. Thanks.

Hi Designers

Would like to see a design that combines the layout format of the bottom half of 1234602 ( easy to read) and the top half of 1227356 ( like the pictures in this one).

Also, want to replace "Marketing....." with Side #1 " Providing residential/stratas with quality, affordable cleaning, caretaking and concierge services.. and then the rest of the text in point/bullet form.

With side #2, want to replace " Marketing...." with "Providing quality, affordable commercial janitorial service to....

                                   

 

Please use latest pictures uploaded. The designs we've liked so far have 1 large picture ( picture of buildings ) on each side with 2-3 smaller pics in various layouts. i.e. for side 1 : Cleaning ( a picture of a cleaner ) Caretaking ( picture of handyman in white shaking hand) Concierge ( picture of person at a desk on the phone)

The font should be large and easy to read. We also like the designs where key points are in point form.

The company name and logo and contact info should be easy to read.

We did like one design using vector characters but think they should only be incorporated as part of the overall design

Target Market(s)

Property Managers, Building Owners, Multicultural Decision makers, aged 28 - 60, very busy people

Industry/Entity Type

Janitorial Service

Requirements
Must have
• 2 pages, 8 1/2 x 11 ( double sided) but can be used separately
Nice to have
• Would like to be able to change photos for different campaigns

```html
<!DOCTYPE html>
<html lang="en">
<head>
<meta charset="utf-8">
<title>Harbor Tidy Works Inc. – Building Services Flyers</title>
<link href="https://fonts.googleapis.com/css2?family=Ubuntu:wght@400;500&display=swap" rel="stylesheet">
<style>
  :root{
    --canvas:#eef8fe;
    --paper:#ffffff;
    --ink:#111111;
    --leaf:#8dc63f;
    --forest:#006837;
    --sky:#00aeef;
    --navy:#283891;
    --res-photo-a:#2f7fc4;
    --res-photo-b:#c9d9e6;
    --com-photo-a:#1c6fae;
    --com-photo-b:#7cc04a;
  }
  *{box-sizing:border-box;margin:0;padding:0}
  html,body{width:1200px;height:1000px;overflow:hidden}
  body{background:var(--canvas);font-family:"Ubuntu",Arial,sans-serif;position:relative}
  .flyer{position:absolute;top:215px;width:444px;height:570px;background:var(--paper);
    box-shadow:2px 3px 6px rgba(40,60,90,.35);overflow:hidden}
  .flyer--residential{left:151px}
  .flyer--commercial{left:606px}
  .brand{position:absolute;left:20px;top:82px;width:178px;font-size:19px;font-weight:500;
    color:var(--ink);letter-spacing:-.2px;white-space:nowrap}
  .service-tag{position:absolute;left:207px;top:28px;width:234px;height:100px;color:#fff;
    font-size:20px;line-height:27px;padding:10px 0 0 20px}
  .flyer--residential .service-tag{background:var(--leaf)}
  .flyer--commercial .service-tag{background:var(--sky);width:233px}
  .hero{position:absolute;left:0;top:156px;width:100%;height:126px}
  .flyer--residential .hero{background:linear-gradient(180deg,var(--res-photo-a),#6aa8d8 60%,var(--res-photo-b))}
  .flyer--commercial .hero{background:linear-gradient(100deg,#0d5a94,var(--com-photo-a) 55%,#5aa6d6 75%,var(--com-photo-b))}
  .headline{position:absolute;left:0;top:294px;width:100%;text-align:center;font-size:23px;font-weight:500}
  .flyer--residential .headline{color:var(--forest)}
  .flyer--commercial .headline{color:var(--navy)}
  .points{position:absolute;list-style:none;text-align:right;font-size:13px;line-height:16.8px}
  .flyer--residential .points{right:22px;top:342px;color:var(--forest)}
  .points .fine{font-size:9px}
  .inset-photo{position:absolute;left:0;top:397px;width:200px;height:124px}
  .flyer--residential .inset-photo{background:linear-gradient(180deg,#3d86c6,#a9c7de 45%,#e6dfd6)}
  .flyer--commercial .inset-photo{background:linear-gradient(180deg,#cfd6d8,#8c9799 55%,#5f6a6c)}
  .callout{position:absolute;right:22px;top:476px;text-align:right;color:var(--forest);font-size:13px;line-height:17px}
  .footer-bar{position:absolute;left:0;bottom:0;width:100%;height:32px;color:#fff;font-size:13px;
    text-align:center;line-height:32px}
  .flyer--residential .footer-bar{background:var(--forest)}
  .flyer--commercial .footer-bar{background:var(--navy)}
  .frequency{position:absolute;left:18px;top:342px;color:var(--navy);font-size:13px;line-height:15px}
  .frequency .fine{font-size:10px;line-height:13px}
  .specs{position:absolute;right:14px;top:342px;text-align:right;color:var(--navy);font-size:13px;line-height:16.8px;list-style:none}
  .benefits{position:absolute;right:14px;top:443px;text-align:right;color:var(--navy);font-size:13px;line-height:13px}
  .benefits .fine{font-size:10px}
  .benefits .lead{display:block;margin-bottom:2px}
  .benefits .call{display:block;margin-top:3px}
</style>
</head>
<body>

<section class="flyer flyer--residential">
  <div class="brand">Harbor Tidy Works</div>
  <div class="service-tag">RESIDENTIAL /<br>STRATA<br>BUILDING SERVICES</div>
  <div class="hero" role="img" aria-label="Photo of residential high-rise towers against a blue sky"></div>
  <h2 class="headline">CLEANING | CARETAKING | CONCIERGE</h2>
  <ul class="points">
    <li># 1 PRIORITY <span class="fine">- CUSTOMER SERVICE &amp; COMMUNICATION</span></li>
    <li>OVER 20 YEARS INDUSTRY EXPERIENCE</li>
    <li>TRAINED, COUTEOUS STAFF</li>
    <li>100% GREEN CHEMICALS</li>
    <li>Servicing greater vancouver</li>
    <li>AFFORDABLE, QUALITY SERVICE</li>
  </ul>
  <div class="inset-photo" role="img" aria-label="Photo of a low-rise condominium building"></div>
  <p class="callout">NEW CONSTRUCTION?<br>WE DO MOVE-INS/OUTS</p>
  <footer class="footer-bar">CALL 604-555-0142 &nbsp;|&nbsp; dale@harbortidyworks.com</footer>
</section>

<section class="flyer flyer--commercial">
  <div class="brand">Harbor Tidy Works</div>
  <div class="service-tag">COMMERCIAL<br>BUILDING<br>SERVICES</div>
  <div class="hero" role="img" aria-label="Photo of a glass office roof with green leaves"></div>
  <h2 class="headline">NIGHT TIME JANITORIAL SERVICE</h2>
  <p class="frequency">DAILY OR WEEKLY SERVICE<br><span class="fine">500 – 200,00 SQUARE FEET<br>100% GREEN CLEANING</span></p>
  <ul class="specs">
    <li>CUSTOMIZED SPECIFICATIONS</li>
    <li>STRUCTURED SUPERVISION</li>
    <li>24/7</li>
    <li>SYSTEMATIC QUALITY</li>
    <li>ASSURANCE (QA) AUDITS</li>
  </ul>
  <div class="inset-photo" role="img" aria-label="Photo of a clean office cafeteria with a mop bucket and wet floor sign"></div>
  <p class="benefits">
    <span class="lead">NO MORE CLEANING HEADACHES!</span>
    <span class="fine">CSPA CLEANING PRODUCTION RATES<br>20 YEARS EXPERIENCE<br>AFFORDABLE, QUALITY SERVICE<br>TRAINED,COURTEOUS STAFF</span>
    <span class="call">CALL 604-555-0142</span>
  </p>
  <footer class="footer-bar">CALL 604-555-0142 &nbsp;|&nbsp; dale@harbortidyworks.com</footer>
</section>

</body>
</html>
```